Ferris + Oakdale Architecture Ltd Stationary rebrand Lead designer to create a fresh clean modern...

We have recieved a great new logo design and now we are after a consistant fresh and modern stationary to match the new design. Business card design, Letter Head design, presentatnion folders and other stationery within the package. I have also added some of our existing layouts for presentation we would like updating with the new look, We would like a clean modern fresh design that looks visually pleasing on the page. we cant wait to see what you come up with!!!!

Target Market(s)

young professionals and middle age clients

Industry/Entity Type

Architect

Contact Information for Business Card

i have uploarded our orginal business card that has all the details attached.

Font styles to use
Sans Serif

Colors
000000
ffffff
d3d3d3

Requirements
Must have
• Logo and our contact information
Nice to have
• white sape around the card to give a clean look.

```html
<!DOCTYPE html>
<html lang="en">
<head>
<meta charset="utf-8">
<title>Ferris + Oakdale Architecture – Business Card</title>
<link rel="stylesheet" href="https://fonts.googleapis.com/css2?family=Poppins:wght@300;400;500&family=Roboto:wght@400&display=swap">
<style>
  :root {
    --ink: #000000;
    --paper: #ffffff;
    --stage: #e4e4e4;
    --muted: #b8b8b8;
    --body: #555555;
    --rule: #d3d3d3;
    --card-dark: #0b0d0e;
  }
  * { margin: 0; padding: 0; box-sizing: border-box; }
  html, body {
    width: 1200px; height: 1200px; overflow: hidden;
    background: var(--stage);
    font-family: "Poppins", sans-serif;
  }
  .canvas { position: relative; width: 1200px; height: 1200px; }
  .card {
    position: absolute; left: 262px; width: 686px; height: 392px;
  }
  .card--front { top: 165px; background: var(--paper); }
  .card--back { top: 653px; background: var(--card-dark); }

  /* Front: brand block */
  .brand {
    position: absolute; left: 65px; top: 126px; width: 232px;
    display: flex; flex-direction: column; align-items: center;
    color: var(--ink); font-weight: 500;
  }
  .brand__mark { width: 96px; height: 96px; background: var(--ink); margin-bottom: 13px; }
  .brand__name { font-size: 20px; letter-spacing: 2.6px; line-height: 1; white-space: nowrap; }
  .brand__sub { font-size: 10px; letter-spacing: 12px; margin-top: 8px; margin-right: -12px; line-height: 1; white-space: nowrap; }

  .divider {
    position: absolute; left: 328px; top: 79px; width: 1px; height: 240px;
    background: linear-gradient(to bottom, transparent, var(--rule) 15%, var(--rule) 85%, transparent);
  }

  .details { position: absolute; left: 349px; top: 80px; }
  .details__name { font-size: 27px; font-weight: 500; color: var(--ink); line-height: 1.1; }
  .details__role { font-size: 17px; font-weight: 400; color: var(--muted); line-height: 1.2; }
  .details__address { margin-top: 13px; font-size: 17px; font-weight: 400; color: var(--body); line-height: 21px; }
  .details__address .po { margin-top: 4px; }
  .contact { list-style: none; margin-top: 11px; }
  .contact li {
    display: flex; align-items: center; gap: 12px;
    font-size: 17px; font-weight: 400; color: var(--body); line-height: 22px;
  }
  .contact svg { width: 15px; height: 15px; flex: none; fill: var(--ink); }

  /* Back */
  .back-brand {
    position: absolute; left: 0; right: 0; top: 112px;
    display: flex; flex-direction: column; align-items: center;
    color: var(--paper); font-weight: 500;
  }
  .back-brand__mark { width: 96px; height: 96px; background: var(--paper); margin-bottom: 22px; }
  .back-brand__name { font-size: 22px; letter-spacing: 3px; line-height: 1; }
  .back-web {
    position: absolute; left: 0; right: 0; top: 328px; text-align: center;
    font-family: "Roboto", sans-serif; font-size: 16px; letter-spacing: 2.6px;
    color: var(--paper);
  }
</style>
</head>
<body>
<main class="canvas">
  <section class="card card--front" aria-label="Business card front">
    <div class="brand">
      <span class="brand__mark"></span>
      <span class="brand__name">FERRIS + OAKDALE</span>
      <span class="brand__sub">ARCHITECTURE</span>
    </div>
    <div class="divider"></div>
    <div class="details">
      <h1 class="details__name">Daniel Ferris</h1>
      <p class="details__role">Director</p>
      <div class="details__address">
        <p>42 Harlow Street</p>
        <p>Kingsford 7810</p>
        <p class="po">PO Box 5184, Kingsford 7843</p>
      </div>
      <ul class="contact">
        <li><svg viewBox="0 0 24 24"><path d="M6.6 10.8a15.1 15.1 0 0 0 6.6 6.6l2.2-2.2c.3-.3.7-.4 1-.2 1.1.4 2.3.6 3.6.6.6 0 1 .4 1 1V20c0 .6-.4 1-1 1C10.6 21 3 13.4 3 4c0-.6.4-1 1-1h3.5c.6 0 1 .4 1 1 0 1.3.2 2.5.6 3.6.1.3 0 .7-.2 1z"/></svg>03 555 0142</li>
        <li><svg viewBox="0 0 24 24"><path d="M7 1h10a2 2 0 0 1 2 2v18a2 2 0 0 1-2 2H7a2 2 0 0 1-2-2V3a2 2 0 0 1 2-2zm0 3v15h10V4zm5 16.2a.9.9 0 1 0 0 1.8.9.9 0 0 0 0-1.8z"/></svg>0270 555 318</li>
        <li><svg viewBox="0 0 24 24"><path d="M2 5h20v14H2zm2 2v.5l8 5 8-5V7zm0 2.8V17h16V9.8l-8 5z"/></svg>daniel@foarchitecture.co.nz</li>
        <li><svg viewBox="0 0 24 24"><path d="M12 2a10 10 0 1 0 0 20 10 10 0 0 0 0-20zm-1 17.9A8 8 0 0 1 4.2 10.8L9 15.6v1c0 1.1.9 2 2 2zm6.9-2.5a2 2 0 0 0-1.9-1.4h-1v-3c0-.6-.4-1-1-1H8v-2h2c.6 0 1-.4 1-1V7h2a2 2 0 0 0 2-2v-.4a8 8 0 0 1 2.9 12.8z"/></svg>www.foarchitecture.co.nz</li>
      </ul>
    </div>
  </section>

  <section class="card card--back" aria-label="Business card back">
    <div class="back-brand">
      <span class="back-brand__mark"></span>
      <span class="back-brand__name">FERRIS + OAKDALE</span>
    </div>
    <p class="back-web">www.foarchitecture.co.nz</p>
  </section>
</main>
</body>
</html>
```